Sign listing benefits of Wash and Fold Service

Sign 48 inches wide and 24 inches height to showcase service listed above.
Benefits include:
Saves Money
Saves Time
Convenient
Stain Treatment

Looking for something colorful (Blue and white are our business colors) the look of a laundromat business.

```html
<!DOCTYPE html>
<html lang="en">
<head>
<meta charset="utf-8">
<title>Wash and Fold Service – Benefits Sign</title>
<link href="https://fonts.googleapis.com/css2?family=Bebas+Neue&family=Poppins:wght@400;700&display=swap" rel="stylesheet">
<style>
  :root {
    --navy: #0a3a66;
    --blue: #0f74bf;
    --bright: #2ea3f2;
    --sky: #6cbcff;
    --white: #ffffff;
    --photo-a: #2f5f8c;
    --photo-b: #5a86ad;
  }
  html, body { margin: 0; padding: 0; overflow: hidden; }
  body { width: 1200px; height: 600px; background: var(--white); }
  .sign { position: relative; width: 1200px; height: 600px; overflow: hidden; background: var(--white); }
  .backdrop, .art { position: absolute; inset: 0; }
  .headline {
    position: absolute; left: 124px; top: 222px; margin: 0;
    font-family: "Poppins", sans-serif; font-weight: 700;
    font-size: 62px; line-height: 72px; letter-spacing: -0.5px;
    color: var(--white);
  }
  .headline .accent { display: block; color: var(--sky); }
  .benefits-title {
    position: absolute; top: 60px; left: 792px; width: 375px;
    display: flex; align-items: center; justify-content: space-between;
  }
  .benefits-title h2 {
    margin: 0; font-family: "Bebas Neue", sans-serif; font-weight: 400;
    font-size: 72px; line-height: 72px; color: var(--navy); letter-spacing: 0.5px;
  }
  .rule { width: 78px; height: 5px; background: linear-gradient(90deg, transparent, #5db6f5 30%, #5db6f5 70%, transparent); }
  .benefit-list { list-style: none; margin: 0; padding: 0; }
  .benefit {
    position: absolute; left: 780px; width: 420px; height: 64px;
    display: flex; align-items: center; padding-left: 29px; box-sizing: border-box;
    font-family: "Poppins", sans-serif; font-size: 29px; color: var(--white);
  }
  .benefit.dark { background: linear-gradient(90deg, var(--navy) 0%, var(--navy) 45%, rgba(10,58,102,0) 100%); }
  .benefit.light { background: linear-gradient(90deg, var(--blue) 0%, var(--blue) 40%, rgba(15,116,191,0) 100%); }
</style>
</head>
<body>
<main class="sign">
  <svg class="backdrop" width="1200" height="600" viewBox="0 0 1200 600">
    <defs>
      <linearGradient id="photoTone" x1="0" y1="0" x2="1" y2="1">
        <stop offset="0" stop-color="var(--photo-b)"/>
        <stop offset="0.5" stop-color="var(--photo-a)"/>
        <stop offset="1" stop-color="#3e6d97"/>
      </linearGradient>
      <linearGradient id="linenTone" x1="0" y1="0" x2="0" y2="1">
        <stop offset="0" stop-color="#ffffff"/>
        <stop offset="0.6" stop-color="#f1f3f5"/>
        <stop offset="1" stop-color="#e6e9ec"/>
      </linearGradient>
    </defs>
    <rect x="700" y="0" width="500" height="600" fill="url(#linenTone)" role="img" aria-label="Soft photo of neatly folded white laundry"/>
    <path d="M0 0 H470 C620 100 705 260 705 600 H0 Z" fill="url(#photoTone)" role="img" aria-label="Blue-tinted photo of a steam iron pressing clothes"/>
    <path d="M470 0 C620 100 705 260 705 600" fill="none" stroke="var(--navy)" stroke-width="22"/>
  </svg>

  <svg class="art" width="1200" height="600" viewBox="0 0 1200 600">
    <defs>
      <linearGradient id="badge" x1="0" y1="0" x2="1" y2="1">
        <stop offset="0" stop-color="var(--bright)"/>
        <stop offset="1" stop-color="#0b66b3"/>
      </linearGradient>
    </defs>
    <g class="icon money">
      <circle cx="541" cy="55" r="64" fill="var(--white)"/>
      <circle cx="541" cy="55" r="56" fill="url(#badge)"/>
      <g fill="none" stroke="var(--white)" stroke-width="3.5" stroke-linecap="round" stroke-linejoin="round">
        <path d="M533 18 l5 7 h8 l5-7 z"/>
        <path d="M536 26 c-16 8 -22 22 -18 34 c3 8 12 10 24 10 c12 0 21-2 24-10 c4-12 -2-26 -18-34"/>
        <path d="M504 66 h8 v20 h-8 z"/>
        <path d="M512 70 c8-4 14-4 20 0 h10 c4 0 4 6 0 6 h-14 M512 84 c10 4 18 6 26 2 l28-16 c4-3 0-8-4-6 l-20 10"/>
      </g>
      <text x="543" y="53" text-anchor="middle" font-family="Poppins, sans-serif" font-weight="700" font-size="18" fill="var(--white)">$</text>
    </g>
    <g class="icon speed">
      <circle cx="649" cy="190" r="64" fill="var(--white)"/>
      <circle cx="649" cy="190" r="56" fill="url(#badge)"/>
      <g fill="none" stroke="var(--white)" stroke-width="4" stroke-linecap="round">
        <path d="M638 166 h24 a24 24 0 0 1 0 48 h-30"/>
        <path d="M661 197 l10-12"/>
        <path d="M625 175 h16 M615 184 h18 M607 192 h22 M614 200 h16 M622 208 h10"/>
      </g>
    </g>
    <g class="icon check">
      <circle cx="698" cy="368" r="64" fill="var(--white)"/>
      <circle cx="698" cy="368" r="56" fill="url(#badge)"/>
      <path d="M668 368 l18 22 l36-48 v20 l-36 30 z" fill="var(--white)"/>
      <path d="M668 370 l18 22 l38-52" fill="none" stroke="var(--white)" stroke-width="9" stroke-linejoin="round"/>
    </g>
    <g class="icon sparkle">
      <circle cx="687" cy="541" r="64" fill="var(--white)"/>
      <circle cx="687" cy="541" r="56" fill="url(#badge)"/>
      <g fill="var(--white)">
        <path d="M677 510 q3 14 17 17 q-14 3 -17 17 q-3-14 -17-17 q14-3 17-17 z"/>
        <path d="M703 532 q4 18 20 21 q-16 3 -20 21 q-4-18 -20-21 q16-3 20-21 z"/>
        <path d="M671 556 q2 9 10 11 q-8 2 -10 11 q-2-9 -10-11 q8-2 10-11 z"/>
      </g>
    </g>
  </svg>

  <h1 class="headline">Wash and<span class="accent">Fold Service</span></h1>

  <div class="benefits-title">
    <span class="rule"></span>
    <h2>Benefits</h2>
    <span class="rule"></span>
  </div>

  <ul class="benefit-list">
    <li class="benefit dark" style="top:179px">Saves Money</li>
    <li class="benefit light" style="top:274px">Saves Time</li>
    <li class="benefit dark" style="top:369px">Convenient</li>
    <li class="benefit light" style="top:465px">Stain Treatment</li>
  </ul>
</main>
</body>
</html>
```